Brochure for Specialist Divorce Support

1. I want an A4 three fold brochure or DL to promote my business and services.
My market are people going through divorce and are usually feeling very overwhelmed and therefore not functioning very well - both men and women, age early forties,
2. Colours – variety of blues and lime greens but you choose if you need a contrast e.g. orange
3. Images – happy single families
4. Theme - could you make it around water please - soothing
5. Logos – HWN &; HWT (I will attach)
6. I have a lot of content so maybe not too busy but still professional feel +
warm and reassuring
7. I'm attaching -

- a draft brochure I put together using a Microsoft template
- a word document with extra details
- plus two logos to do with my qualifications
- and some images for you to choose from

7. I want to use this as a template for some other brochures -> more work for
the winner.

Target Market(s)

Men and women usually in their early forties with primary school aged children i.e 5 to 12 years old.
They are going through a divorce and very upset, Maybe losing contact with their children and their way of life as they know it is disappearing. They are in turmoil and not functioning as well as they usually do.

Industry/Entity Type

Business

Font styles to use
Sans Serif

Colors
34a7d7
abd037
3277b5

Requirements
Must have
• I want the brochure to be three folds with the center the full A4
• Could you make the theme around water please.
• I will upload some photos for you to use if you want,

```html
<!DOCTYPE html>
<html lang="en">
<head>
<meta charset="utf-8">
<title>Specialist Divorce Support – Tri-fold Brochure</title>
<link href="https://fonts.googleapis.com/css2?family=Open+Sans:wght@400;600;700&display=swap" rel="stylesheet">
<style>
  :root{
    --sky:#34a7d7;
    --lime:#abd037;
    --ocean:#3277b5;
    --deep:#1f5f9a;
    --ink:#1d3550;
    --mist:#eaf4fa;
    --white:#ffffff;
    --page:#d4d6d8;
  }
  *{box-sizing:border-box;margin:0;padding:0}
  html,body{width:1200px;height:1200px;overflow:hidden;background:var(--page);font-family:'Open Sans',sans-serif}
  .brochure{position:absolute;left:30px;top:197px;width:1140px;height:806px;display:flex;box-shadow:0 10px 30px rgba(0,0,0,.25)}
  .panel{position:relative;width:380px;height:806px;overflow:hidden;background:var(--white)}
  .panel + .panel{border-left:1px solid rgba(0,0,0,.06)}
  .panel-bg{position:absolute;inset:0;width:100%;height:100%}
  .content{position:absolute}

  /* Inside panel */
  .section-title{color:var(--ocean);font-weight:600;font-size:24px;line-height:1.2;padding-bottom:4px;border-bottom:2px solid var(--sky);display:inline-block;margin-bottom:10px}
  .services{left:30px;top:40px;width:330px}
  .service-list{list-style:none;font-size:12px;line-height:1.42;color:var(--ink)}
  .service-list li{position:relative;padding-left:12px;margin-bottom:3px}
  .service-list li::before{content:"";position:absolute;left:0;top:7px;width:5px;height:5px;border-radius:50%;background:var(--sky)}
  .testimonial{left:30px;top:365px;width:320px}
  .testimonial p{font-size:12px;line-height:1.42;color:var(--ink);margin-bottom:7px}

  /* Middle panel */
  .brand-stack{left:0;top:310px;width:380px;text-align:center}
  .brand{display:inline-flex;align-items:center;gap:10px;font-weight:700;color:var(--ocean);font-size:34px;letter-spacing:2px}
  .brand-dot{width:16px;height:16px;border-radius:50%;background:var(--ocean)}
  .brand.small{font-size:24px;margin-top:18px}
  .brand-square{width:14px;height:14px;background:var(--ocean)}
  .contact{left:40px;top:560px;width:320px;color:var(--white);text-align:center;text-shadow:0 1px 2px rgba(10,50,90,.45)}
  .contact h2{font-size:28px;font-weight:600;padding-bottom:8px;border-bottom:2px solid var(--white);margin-bottom:12px}
  .contact p{font-size:14.5px;line-height:1.7}

  /* Cover */
  .cover-brand{left:0;top:52px;width:380px;text-align:center}
  .headline{left:20px;top:505px;width:340px;text-align:center}
  .headline h1{font-weight:700;line-height:1.15;font-size:30px}
  .headline .line-a{display:block;color:var(--white)}
  .headline .line-b{display:block;color:var(--deep)}
  .headline hr{border:0;border-top:2px solid var(--white);width:280px;margin:10px auto 12px}
  .headline p{color:var(--ink);font-size:15px;line-height:1.45}
  .url-pill{display:inline-block;margin-top:22px;background:var(--white);color:var(--deep);font-weight:700;font-size:18px;padding:8px 34px;border-radius:20px;box-shadow:0 3px 6px rgba(0,0,0,.25)}
</style>
</head>
<body>
<main class="brochure">

  <!-- Inside panel: services & testimonial -->
  <section class="panel panel-inside">
    <svg class="panel-bg" viewBox="0 0 380 806" preserveAspectRatio="none">
      <defs>
        <linearGradient id="waterLight" x1="0" y1="0" x2="0" y2="1">
          <stop offset="0" stop-color="#dbeef8"/><stop offset=".6" stop-color="#f4f9fc"/><stop offset="1" stop-color="#ffffff"/>
        </linearGradient>
        <linearGradient id="beachFamily" x1="0" y1="0" x2="0" y2="1">
          <stop offset="0" stop-color="#8ec7ea"/><stop offset=".5" stop-color="#c9e3f1"/><stop offset="1" stop-color="#d9cdb8"/>
        </linearGradient>
      </defs>
      <rect width="380" height="806" fill="url(#waterLight)"/>
      <path d="M0 806 L0 792 C140 778 290 748 380 690 L380 806 Z" fill="var(--lime)"/>
      <path d="M50 806 C170 790 300 760 380 710 L380 806 Z" fill="url(#beachFamily)" role="img" aria-label="Photo of a mother and two sons walking barefoot along the beach"/>
    </svg>
    <div class="content services">
      <h2 class="section-title">Our Services:</h2>
      <ul class="service-list">
        <li>Specialist divorce support to suit your needs</li>
        <li>Pre-mediation coaching helping you prepare and achieve more positive outcomes to avoid going to court</li>
        <li>Collaborative law coaching to increase crucial skills so you can participate more constructively in negotiations</li>
        <li>Delivery of HWN Healthy Words Navigator giving you real feedback on the constructive and destructive behaviours you choose during conflict situations to facilitate more productive discussions</li>
        <li>Corporate Conflict Management Training</li>
      </ul>
    </div>
    <div class="content testimonial">
      <h2 class="section-title">Testimonial :</h2>
      <p>After many cups of coffee and long hours of listening to me, my very good friend suggested I speak to Helen, a divorce coach. I was a bit skeptical, especially when a phone session was suggested.</p>
      <p>From my first phone session I felt empowered. It gave me a sense of direction, assisted me to set realistic goals and action plans. Most importantly it aided my self esteem.</p>
      <p>Divorce is overwhelming. Talking to a caring professional like Miranda helped me acknowledge my priorities and a way to achieve them.</p>
      <p>Thank you Miranda." Lucia - Cccccc, Smmmmm. AAA</p>
    </div>
  </section>

  <!-- Middle panel: brands & contact -->
  <section class="panel panel-contact">
    <svg class="panel-bg" viewBox="0 0 380 806" preserveAspectRatio="none">
      <defs>
        <linearGradient id="seaFade" x1="0" y1="0" x2="0" y2="1">
          <stop offset="0" stop-color="#c8e1ef"/><stop offset=".7" stop-color="#eef6fa"/><stop offset="1" stop-color="#ffffff"/>
        </linearGradient>
        <linearGradient id="contactBand" x1="0" y1="0" x2="0" y2="1">
          <stop offset="0" stop-color="#2a8fc6"/><stop offset=".7" stop-color="#2f9bd0"/><stop offset="1" stop-color="#5fb6e0"/>
        </linearGradient>
      </defs>
      <rect width="380" height="300" fill="url(#seaFade)" role="img" aria-label="Soft photo of calm shoreline water"/>
      <path d="M0 540 C120 500 260 490 380 500 L380 806 L0 806 Z" fill="url(#contactBand)"/>
      <rect x="0" y="762" width="380" height="44" fill="#a9d5ee" opacity=".8" role="img" aria-label="Photo of waves breaking on the beach"/>
    </svg>
    <div class="content brand-stack">
      <div class="brand"><span class="brand-dot"></span>HWT</div><br>
      <div class="brand small"><span class="brand-square"></span>HWN</div>
    </div>
    <div class="content contact">
      <h2>CONTACT US :</h2>
      <p>EMAIL: hello@harbourway.example</p>
      <p>CALL : 123 456 7890</p>
      <p>Fax : 123 456 7890</p>
      <p>Address : Lorem Ipsum is simply dummy text of the printing</p>
    </div>
  </section>

  <!-- Cover panel -->
  <section class="panel panel-cover">
    <svg class="panel-bg" viewBox="0 0 380 806" preserveAspectRatio="none">
      <defs>
        <linearGradient id="coverBlue" x1="0" y1="0" x2="1" y2="1">
          <stop offset="0" stop-color="var(--sky)"/><stop offset="1" stop-color="#1f6fa6"/>
        </linearGradient>
        <linearGradient id="coverLime" x1="0" y1="0" x2="0" y2="1">
          <stop offset="0" stop-color="#8fbf2c"/><stop offset=".5" stop-color="var(--lime)"/><stop offset="1" stop-color="#7fb127"/>
        </linearGradient>
        <linearGradient id="hugPhoto" x1="0" y1="0" x2="0" y2="1">
          <stop offset="0" stop-color="#a9c3cf"/><stop offset=".6" stop-color="#c8b8a4"/><stop offset="1" stop-color="#a89682"/>
        </linearGradient>
      </defs>
      <rect width="380" height="806" fill="url(#coverBlue)"/>
      <path d="M0 0 L380 0 L380 40 C250 20 80 40 0 120 Z" fill="#4db6e2"/>
      <path d="M0 20 C120 -5 300 10 380 60 L380 200 C300 150 150 140 0 210 Z" fill="#f2f8fb"/>
      <path d="M0 500 C80 470 220 480 380 420 L380 806 L0 806 Z" fill="url(#coverLime)"/>
      <circle cx="200" cy="300" r="180" fill="var(--ocean)"/>
      <circle cx="200" cy="300" r="172" fill="var(--white)"/>
      <circle cx="200" cy="300" r="162" fill="url(#hugPhoto)" role="img" aria-label="Photo of a father hugging his son and daughter at the beach"/>
    </svg>
    <div class="content cover-brand">
      <div class="brand"><span class="brand-dot"></span>HWT</div>
    </div>
    <div class="content headline">
      <h1><span class="line-a">SPECIALIST</span><span class="line-b">DIVORCE SUPPORT</span></h1>
      <hr>
      <p>Helping you move through this major life challenge so you can more successfully start living your new life – your way!</p>
      <span class="url-pill">www.harbourway.example</span>
    </div>
  </section>

</main>
</body>
</html>
```